Packaging Label Design for Eyelash Extension Adhesive

I need labels designed for my new adhesive I just came out with. This is adhesive for eyelash extensions. I already have my logo and love it and want it incorporated in the label.
This is Medical Grade Very low fume adhesive geared towards sensitive clients but yet so great it can be your regular adhesive for everyone not just your sensitive clients.
The attached files I did myself and I do actually really Love but want it tweaked and more professional lookin and smooth out the lines etc.... it looks grainey and want it crisp and clear. The two design I created are the look and feel for my business.

Target Market(s)

Licensed beauty professionals, certified Lash Artist

Industry/Entity Type

Business

Font styles to use
Sans Serif
Decorative
Script

Colors
6b449b

Requirements
Must have
• My Verna Brow logo, the colors plum and white
• the fonts and look of label to be elegant & stylish
• I love the bracket { } look with ribbon behind it like wrapped around the bottle of adhesvive. which is only 10ml so it is a fairly small bottle
• ***FORGOT TO ADD THAT NEEDS THE LABEL TO EITHER HAVE A FRONT AND BACK 2 SEPERATE STICKERS OR JUST 1 LONG LABEL TO WRAP AROUND THE 10ML BOTTLE, NEED TO ADD INGREDIENTS AND MY BUSINESS INFO ON BACK OF LABEL. IF ONE LABEL IT NEEDS TO BE 1.25"HEIGHT X 3.40" LONG OR 1.25" X 1.5 TWICE

```html
<!DOCTYPE html>
<html lang="en">
<head>
<meta charset="utf-8">
<title>Velvet Calm – Lash Adhesive Label</title>
<link rel="stylesheet" href="https://fonts.googleapis.com/css2?family=Arimo&family=Cinzel:wght@400;600&family=Great+Vibes&family=Marcellus&display=swap">
<style>
  :root {
    --plum-deep: #3f1f5c;
    --plum: #6b449b;
    --plum-bright: #6a2fa0;
    --plum-light: #b48ad6;
    --plum-ink: #3a1260;
    --white: #ffffff;
    --silver: #d9d9dd;
    --silver-dark: #bdbdc3;
  }
  * { margin: 0; padding: 0; box-sizing: border-box; }
  html, body { width: 1200px; height: 441px; overflow: hidden; background: var(--plum-deep); }
  .label {
    position: relative;
    width: 1200px; height: 441px; overflow: hidden;
    background:
      radial-gradient(ellipse 520px 300px at 600px 200px, rgba(180,138,214,.55), transparent 70%),
      linear-gradient(180deg, #4a2466 0%, #6b449b 45%, #5a3283 70%, #3f1f5c 100%);
    font-family: "Arimo", Arial, sans-serif;
  }
  .ribbon {
    position: absolute; left: 0; top: 186px; width: 1200px; height: 86px; z-index: 1;
    background: linear-gradient(180deg, var(--silver-dark) 0%, var(--white) 30%, var(--white) 60%, var(--silver) 100%);
    border-top: 2px solid var(--white);
    border-bottom: 2px solid var(--white);
  }
  .plaque { position: absolute; left: 0; top: 0; width: 640px; height: 441px; z-index: 2; }
  .front-text { position: absolute; z-index: 3; }
  .brand-name {
    left: 120px; width: 390px; top: 138px; text-align: center;
    font-family: "Cinzel", serif; font-weight: 400; font-size: 26px; letter-spacing: 1px;
    color: var(--white);
  }
  .brand-rule {
    height: 2px; left: 185px; width: 260px;
    background: linear-gradient(90deg, transparent, rgba(255,255,255,.6), transparent);
  }
  .brand-rule.top { top: 132px; }
  .brand-rule.bottom { top: 172px; }
  .tagline {
    left: 100px; width: 430px; top: 183px; text-align: center;
    font-family: "Marcellus", serif; font-size: 18px; color: var(--plum-ink);
  }
  .product-name {
    left: 100px; width: 430px; top: 205px; text-align: center;
    font-family: "Cinzel", serif; font-size: 44px; letter-spacing: 2px;
    color: var(--white);
    text-shadow: 0 1px 2px rgba(60,20,90,.7);
  }
  .creator {
    left: 150px; width: 330px; top: 278px; text-align: center;
    font-family: "Great Vibes", cursive; color: var(--white); line-height: .9;
  }
  .creator .by { display: block; font-size: 40px; }
  .creator .name { display: block; font-size: 40px; }

  .back-panel {
    position: absolute; left: 710px; top: 28px; width: 391px; height: 387px;
    border: 2px solid var(--white);
    background: radial-gradient(ellipse 260px 180px at 50% 30%, #b48ad6 0%, #7c4fad 50%, #5a3283 100%);
  }
  .back-text { position: absolute; z-index: 3; }
  .ingredients-title { left: 14px; top: 12px; font-size: 16px; color: var(--white); }
  .back-name {
    left: 0; width: 100%; top: 166px; text-align: center;
    font-family: "Cinzel", serif; font-size: 34px; letter-spacing: 2px; color: var(--plum-bright);
  }
  .back-tagline {
    left: 0; width: 100%; top: 212px; text-align: center;
    font-family: "Marcellus", serif; font-size: 15px; color: var(--plum-ink);
  }
  .back-facts {
    left: 12px; right: 28px; top: 256px;
    display: flex; justify-content: space-between; font-size: 16px; color: var(--white);
  }
  .contact {
    left: 0; width: 100%; top: 302px; text-align: center;
    font-size: 16px; color: var(--white); line-height: 26px;
  }
  .website {
    left: 0; bottom: 0; width: 100%; height: 33px;
    background: var(--white); color: var(--plum-deep);
    text-align: center; font-size: 16px; line-height: 33px;
  }
</style>
</head>
<body>
<main class="label">
  <section class="back-panel">
    <div class="back-text ingredients-title">Ingredients :</div>
    <div class="back-text back-name">VELVET CALM</div>
    <div class="back-text back-tagline">Certified Medical Grade Lash Adhesive</div>
    <div class="back-text back-facts"><span>Net Wt. : 10 ML</span><span>MRP : 0.0 $</span></div>
    <div class="back-text contact">Contact us :<br>000.000.0000 &nbsp;|&nbsp; vernabrow@mail.com</div>
    <div class="back-text website">www.vernabrow.com</div>
  </section>

  <div class="ribbon"></div>

  <svg class="plaque" viewBox="0 0 640 441" aria-hidden="true">
    <defs>
      <radialGradient id="plaqueFill" cx="50%" cy="70%" r="65%">
        <stop offset="0%" stop-color="#c9a2e6"/>
        <stop offset="55%" stop-color="#7c4fad"/>
        <stop offset="100%" stop-color="#4e2a74"/>
      </radialGradient>
      <filter id="plaqueGlow" x="-10%" y="-10%" width="120%" height="120%">
        <feDropShadow dx="0" dy="0" stdDeviation="6" flood-color="#8a2fd0" flood-opacity=".8"/>
      </filter>
    </defs>
    <path filter="url(#plaqueGlow)" fill="url(#plaqueFill)" stroke="#ffffff" stroke-width="4"
      d="M 200 92
         Q 255 92 275 62 Q 315 25 355 62 Q 375 92 430 92
         Q 462 92 470 120 Q 478 140 500 140
         Q 530 150 530 225 Q 530 300 500 310
         Q 478 310 470 330 Q 462 358 430 358
         Q 375 358 355 385 Q 315 420 275 385 Q 255 358 200 358
         Q 168 358 160 330 Q 152 310 130 310
         Q 100 300 100 225 Q 100 150 130 140
         Q 152 140 160 120 Q 168 92 200 92 Z"/>
  </svg>

  <div class="front-text brand-rule top"></div>
  <div class="front-text brand-name">Verna Brow</div>
  <div class="front-text brand-rule bottom"></div>
  <div class="front-text tagline">Certified Medical Grade Lash Adhesive</div>
  <div class="front-text product-name">VELVET CALM</div>
  <div class="front-text creator"><span class="by">by</span><span class="name">Mara Vellin</span></div>
</main>
</body>
</html>
```